Create look and feel for existing Web Page

Update Web Page

We have a website at http://www.getmirvo.com/index-web.html. It is a single page html site, with a custom signup form. We also have a zen desk plugin at the bottom of the page. We'd like to redesign the look and feel of the entire site. We sell software to eye doctors. Also called optometrists, our software tool makes it easy for doctors to manage patients, bill, and document patient encounters. I have included our logos below.

We are looking for a new design preferably in HTML 5, CSS etc. The fields on the form on this page: http://www.getmirvo.com/index-web.html

You can get screen shots of our software application at this site: http://staging.getmirvo.com
username: test@sampledomain-mirvo.com
password: password

```html
<!DOCTYPE html>
<html lang="en">
<head>
<meta charset="utf-8">
<title>Mirvo — the practice operating system</title>
<link href="https://fonts.googleapis.com/css2?family=Poppins:wght@300;400;500;600&family=Oswald:wght@200;300&display=swap" rel="stylesheet">
<style>
:root{
  --blue:#0a8fd8;
  --blue-deep:#0b6fb0;
  --blue-dark:#0a5c98;
  --orange:#ff7f11;
  --ink:#333a44;
  --muted:#8a929c;
  --soft:#eef5fb;
  --field:#f2f6fb;
  --sidebar:#2a2d33;
  --panel:#353941;
  --white:#fff;
}
*{margin:0;padding:0;box-sizing:border-box}
html,body{width:1200px;height:3354px;overflow:hidden}
body{position:relative;font-family:'Poppins',sans-serif;color:var(--ink);background:var(--white)}
.abs{position:absolute}
.btn{position:absolute;display:flex;align-items:center;justify-content:center;border-radius:22px;font-size:13px;font-weight:500;color:#fff;background:var(--orange);text-decoration:none}
.btn.outline{background:#fff;color:var(--ink);border:1.5px solid var(--orange);font-size:12px}
.btn.blue{background:var(--blue)}
.center{left:0;width:1200px;text-align:center}

/* hero */
.hero-bg{position:absolute;left:0;top:0}
.logo{position:absolute;font-weight:400;letter-spacing:2px}
.nav-logo{left:128px;top:26px;font-size:34px;color:#fff}
.nav a{position:absolute;top:40px;font-size:14px;color:#fff;text-decoration:none}
.hero-title{left:129px;top:232px;font-size:31px;font-weight:300;line-height:38px;color:#fff}
.hero-title b{font-weight:600}
.hero-text{left:129px;top:320px;width:430px;font-size:13.5px;line-height:21px;color:#e6f2fb;font-weight:300}

/* app preview */
.device{left:600px;top:118px;width:640px;height:446px;background:#fff;border-radius:18px;box-shadow:0 20px 50px rgba(0,40,80,.18)}
.device-base{left:512px;top:560px;width:700px;height:18px;background:linear-gradient(#e4e8ee,#c9cfd8);border-radius:0 0 40px 40px}
.app-side{left:625px;top:143px;width:140px;height:399px;background:var(--sidebar)}
.app-side .brand{position:absolute;left:8px;top:8px;font-size:13px;color:var(--orange);letter-spacing:1px}
.app-side .user{position:absolute;left:0;width:140px;text-align:center;color:#fff;font-size:8px;top:45px}
.app-side .mail{top:58px;color:#888;font-size:6px}
.avatar{position:absolute;left:55px;top:82px;width:32px;height:32px;border-radius:50%;background:#777;border:2px solid #ccc}
.menu{position:absolute;left:6px;width:128px;height:18px;font-size:7px;color:#ddd;padding-left:22px;line-height:18px}
.menu.on{background:var(--blue);border-radius:9px;color:#fff}
.app-main{left:765px;top:143px;width:435px;height:399px;background:#f4f5f7}
.app-top{left:765px;top:143px;width:435px;height:32px;background:#fff;border-bottom:1px solid #e3e5e8;font-size:11px;font-weight:500;padding:9px 0 0 10px}
.chart-box{left:773px;top:178px;width:427px;height:172px;background:#fff}
.chart-box .t{position:absolute;left:5px;top:10px;font-size:9px}
.chart-box .s{position:absolute;left:5px;top:22px;font-size:6px;color:#aaa}
.play{left:879px;top:309px;width:66px;height:66px;border-radius:50%;background:var(--blue);box-shadow:0 6px 18px rgba(10,143,216,.45)}
.stat{top:361px;width:258px;height:103px;background:var(--panel);color:#fff}
.stat h4{position:absolute;left:9px;top:10px;font-size:12px;font-weight:400}
.stat small{position:absolute;left:9px;top:27px;font-size:6px;color:#bbb}
.stat .n{position:absolute;left:9px;top:46px;font-size:22px;font-weight:300}
.stat .tabs{position:absolute;left:0;bottom:6px;width:258px;font-size:6px;color:#ccc}
.stat .tabs span{position:absolute}
.sched{left:773px;top:497px;width:427px;height:40px;background:#fff;font-size:11px;padding:13px 0 0 9px}

/* intro */
.tags{top:693px;font-size:13px;font-weight:500;color:var(--blue)}
.tags i{font-style:normal;margin:0 12px}
.h2{font-size:25px;font-weight:500;line-height:32px;color:var(--ink)}
.feature{position:absolute;top:840px;width:300px;height:70px}
.feature .ic{position:absolute;left:0;top:0;width:64px;height:64px;border-radius:50%;display:flex;align-items:center;justify-content:center}
.feature p{position:absolute;left:80px;top:10px;font-size:16px;line-height:23px;color:#5e6670;font-weight:300}

/* automation */
.photo-work{left:0;top:1058px;width:416px;height:576px;background:linear-gradient(135deg,#f1ede6,#c99a6a 55%,#e2d8cb)}
.ai-title{left:416px;width:696px;top:1092px;text-align:center}
.ai-sub{left:416px;width:696px;top:1168px;text-align:center;font-size:13px;line-height:21px;color:var(--muted);font-weight:300}
.task{position:absolute;width:310px}
.task .ic{position:absolute;left:0;top:0;width:64px;height:64px;border-radius:50%;display:flex;align-items:center;justify-content:center;background:#fff;box-shadow:0 6px 20px rgba(0,0,0,.07)}
.task .ic.on{background:var(--blue);box-shadow:0 8px 20px rgba(10,143,216,.35)}
.task h3{position:absolute;left:80px;top:-7px;font-size:16px;font-weight:500}
.task p{position:absolute;left:80px;top:17px;width:215px;font-size:11.5px;line-height:19px;color:var(--muted);font-weight:300}
.dot{position:absolute;top:1500px;width:10px;height:10px;border-radius:50%;border:1.5px solid var(--blue)}

/* pricing */
.band{left:0;top:2162px;width:1200px;height:640px;background:linear-gradient(180deg,#4d6082 0%,#6e809c 45%,#9aa9bb 75%,#c7ced8 100%)}
.card{position:absolute;top:1857px;width:287px;height:352px;background:#fff;border-radius:4px;box-shadow:0 10px 30px rgba(20,60,110,.1);text-align:center}
.card .name{position:absolute;left:0;width:287px;top:52px;font-size:16px;color:var(--blue);font-weight:500}
.card .pick{position:absolute;left:0;width:287px;top:30px;font-size:12px;color:var(--ink)}
.card hr{position:absolute;left:40px;width:207px;top:86px;border:0;border-top:1px solid #eceff2}
.card .desc{position:absolute;left:40px;width:207px;top:115px;font-size:13px;line-height:21px;color:var(--muted);font-weight:300}
.price{position:absolute;left:0;width:287px;top:200px;font-family:'Oswald',sans-serif;font-weight:200;font-size:42px;color:var(--orange)}
.price sup{font-family:'Poppins',sans-serif;font-size:11px;color:var(--muted);vertical-align:top;position:relative;top:12px;margin-left:6px}
.card .note{position:absolute;left:0;width:287px;top:251px;font-size:10.5px;color:var(--ink)}
.card .btn{left:64px;top:276px;width:160px;height:40px}

.club-small{top:2318px;font-size:12.5px;font-weight:500;color:#fff}
.club-title{top:2358px;font-size:25px;line-height:32px;font-weight:300;color:#fff}

/* form */
.field{position:absolute;background:var(--field);border-radius:20px;font-size:11.5px;color:#9aa3ad;padding:12px 0 0 22px;height:37px}
.chat{left:1107px;top:3175px;width:40px;height:40px;border-radius:50%;background:var(--orange);box-shadow:0 6px 14px rgba(255,127,17,.35);display:flex;align-items:center;justify-content:center}
.footer-line{left:0;top:3273px;width:1200px;border-top:1px solid #eef0f3}
.foot-logo{left:128px;top:3293px;font-size:28px;color:#6b7280}
.copy{left:223px;top:3308px;font-size:11px;color:#8a929c}
.social{position:absolute;top:3307px;width:14px;height:14px;border-radius:50%}
</style>
</head>
<body>

<!-- hero background -->
<svg class="hero-bg" width="1200" height="700" viewBox="0 0 1200 700" aria-hidden="true">
  <defs>
    <linearGradient id="heroGrad" x1="0" y1="0" x2="1" y2="1">
      <stop offset="0" stop-color="#0b7fcc"/>
      <stop offset="1" stop-color="#0a5f9e"/>
    </linearGradient>
    <linearGradient id="heroLight" x1="0" y1="0" x2="1" y2="0">
      <stop offset="0" stop-color="#1697e0"/>
      <stop offset="1" stop-color="#0c86d0"/>
    </linearGradient>
  </defs>
  <path d="M0 0H1200V360C1060 390 930 400 800 470C660 545 520 620 330 640C200 652 90 635 0 612Z" fill="url(#heroGrad)"/>
  <path d="M0 0H460C520 140 500 230 380 290C260 350 110 330 0 380Z" fill="url(#heroLight)" opacity=".55"/>
  <path d="M0 600C200 700 520 680 760 600C900 555 1050 560 1200 620V700H0Z" fill="#fff" opacity="0"/>
</svg>

<div class="logo nav-logo">mirvo</div>
<nav class="nav">
  <a style="left:704px">Home</a>
  <a style="left:789px">Product</a>
  <a style="left:886px">Pricing</a>
</nav>
<a class="btn" style="left:976px;top:29px;width:95px;height:39px;font-size:14px">Sign Up</a>

<h1 class="abs hero-title">Meet <b>Mirvo</b>, the practice<br>operating system</h1>
<p class="abs hero-text">We are lease doctors who got tired of the administration associated with running a lease practice, so instead of complaining we created a system to do it all for us.</p>
<a class="btn" style="left:129px;top:415px;width:224px;height:40px">Get Free Charting Tool</a>

<!-- app preview -->
<div class="abs device-base"></div>
<div class="abs device"></div>
<div class="abs app-side">
  <div class="brand">mirvo</div>
  <svg class="abs" style="left:121px;top:12px" width="10" height="8"><path d="M0 1H10M0 4H10M0 7H10" stroke="#ccc"/></svg>
  <div class="user">Sam Reed</div>
  <div class="user mail">test@sampledomain-mirvo.com</div>
  <div class="avatar"></div>
  <div class="menu on" style="top:122px">Dashboard</div>
  <div class="menu" style="top:142px">Calendar</div>
  <div class="menu" style="top:162px">Search</div>
  <div class="menu" style="top:182px">Settings</div>
  <div class="menu" style="top:202px">Patient Engagement</div>
  <div class="menu" style="top:222px">Logout</div>
</div>
<div class="abs app-main"></div>
<div class="abs app-top">Reed's LLC <span style="font-size:6px;color:#888;font-weight:400">(Active)</span></div>
<div class="abs chart-box">
  <div class="t">Total Patient's Chart : 1</div>
  <div class="s">Daily Appointments</div>
  <svg class="abs" style="left:10px;top:40px" width="417" height="110" aria-hidden="true">
    <path d="M5 5V100H417" stroke="#ddd" fill="none"/>
    <path d="M390 100C400 95 405 60 417 40V100Z" fill="#2a2d33"/>
  </svg>
</div>
<div class="abs play">
  <svg width="66" height="66"><path d="M27 21L46 33L27 45Z" fill="#fff"/></svg>
</div>
<div class="abs stat" style="left:773px">
  <h4>Sales Revenue</h4><small>Lifetime sum of your sales</small>
  <div class="n">0</div>
  <div class="abs" style="right:8px;top:62px;font-size:6px;color:#ddd"><span style="color:#5c5">↗</span> 321(2.05%)</div>
  <div class="tabs"><span style="left:32px">1DAY</span><span style="left:112px">1WEEK</span><span style="left:198px">1MONTH</span></div>
  <div class="abs" style="left:10px;bottom:0;width:70px;height:2px;background:var(--blue)"></div>
</div>
<div class="abs stat" style="left:1048px">
  <h4>Cash Revenue</h4><small>Lifetime sum of your sales</small>
  <div class="n">0</div>
  <div class="tabs"><span style="left:32px">1DAY</span><span style="left:112px">1WEEK</span></div>
  <div class="abs" style="left:10px;bottom:0;width:70px;height:2px;background:var(--blue)"></div>
</div>
<div class="abs sched">Schedule
  <span class="abs" style="left:385px;top:10px;width:32px;height:18px;background:#2a2d33;color:#fff;font-size:6px;padding:5px 0 0 4px">16 Mar</span>
</div>

<!-- intro -->
<svg class="abs" style="left:0;top:780px" width="1200" height="300" aria-hidden="true">
  <path d="M0 110C220 60 420 140 640 110C860 80 1020 40 1200 70V300H0Z" fill="var(--soft)" opacity=".7"/>
  <path d="M0 170C260 130 480 200 720 170C920 145 1060 120 1200 150V300H0Z" fill="#fff" opacity=".8"/>
</svg>
<div class="abs center tags">Simple<i>•</i>Fully Automated<i>•</i>Profitable</div>
<h2 class="abs center h2" style="top:731px">What if running your lease is as simple<br>as a mirvo patient?</h2>

<div class="feature" style="left:128px">
  <div class="ic" style="background:linear-gradient(135deg,#fde1a8,#f7b866)">
    <svg width="26" height="28" fill="none" stroke="#fff" stroke-width="1.8"><circle cx="13" cy="8" r="6"/><path d="M3 27C3 19 8 16 13 16S23 19 23 27M10 16V22H16V16"/></svg>
  </div>
  <p>Designed for lease<br>doctors</p>
</div>
<div class="feature" style="left:456px">
  <div class="ic" style="background:linear-gradient(135deg,#a9cdef,#5b93c9)">
    <svg width="20" height="32" fill="none" stroke="#fff" stroke-width="2"><path d="M10 2V30M16 8C15 5 13 4 10 4 6 4 4 6 4 9 4 16 16 13 16 21 16 24 14 26 10 26 7 26 5 25 4 22"/></svg>
  </div>
  <p>You start with charting<br>@ $49/mon</p>
</div>
<div class="feature" style="left:784px">
  <div class="ic" style="background:linear-gradient(135deg,#a8df7a,#5fb53c)">
    <svg width="28" height="26" fill="none" stroke="#fff" stroke-width="1.8"><path d="M2 11H7V25H2ZM7 12L13 2C15 2 16 4 15 7L14 10H24C26 10 27 12 26 14L23 23C22 25 21 25 19 25H7"/></svg>
  </div>
  <p>Just you &amp; Mirvo can run<br>your lease practice</p>
</div>
<a class="btn" style="left:521px;top:962px;width:158px;height:40px">Sign Up Today!</a>

<!-- automation -->
<div class="abs photo-work" role="img" aria-label="Smiling woman working on a laptop at a bright desk"></div>
<h2 class="abs h2 ai-title">AI to Automate Optometry<br>Office Tasks</h2>
<p class="abs ai-sub">Mirvo uses AI, automation, robots, and other cool technology to streamline<br>office work so you can do things you love</p>

<div class="task" style="left:456px;top:1259px">
  <div class="ic on"><svg width="22" height="22" fill="none" stroke="#fff" stroke-width="1.6"><rect x="2" y="4" width="18" height="16" rx="2"/><path d="M2 9H20M7 2V6M15 2V6M6 13H8M10 13H12M14 13H16M6 16H8M10 16H12M14 16H16"/></svg></div>
  <h3>Schedule</h3>
  <p>Meet your patients where they are, 24 hours 7 days a week with the online scheduler.</p>
</div>
<div class="task" style="left:784px;top:1259px">
  <div class="ic"><svg width="22" height="22" fill="none" stroke="var(--blue)" stroke-width="1.6"><path d="M6 8V2H16V8M6 16H3V8H19V16H16M6 13H16V20H6Z"/></svg></div>
  <h3>Intake</h3>
  <p>Never print out another paper form. Your patients are now able to fill out and sign forms online.</p>
</div>
<div class="task" style="left:456px;top:1379px">
  <div class="ic"><svg width="24" height="24" fill="none" stroke="var(--blue)" stroke-width="1.6"><circle cx="12" cy="12" r="10"/><path d="M12 2V12H22M12 12L5 19"/></svg></div>
  <h3>Chart</h3>
  <p>Start charting all patient findings for FREE. With features like auto population it flies on your mobile phone.</p>
</div>
<div class="task" style="left:784px;top:1379px">
  <div class="ic"><svg width="24" height="26" fill="none" stroke="var(--blue)" stroke-width="1.6"><path d="M15 2H4V24H12M15 2L20 7V12M15 2V7H20M7 11H15M7 15H12M7 19H10M19 15V25M22 17C21 15 16 15 16 18 16 21 22 19 22 22 22 25 17 25 16 23"/></svg></div>
  <h3>Bill</h3>
  <p>Don't waste your precious time or pay someone to bill insurance, let a bot do it for you.</p>
</div>
<div class="dot" style="left:742px;background:radial-gradient(circle,var(--blue) 35%,transparent 40%)"></div>
<div class="dot" style="left:760px"></div>
<div class="dot" style="left:776px"></div>
<a class="btn" style="left:661px;top:1555px;width:207px;height:38px">Get Free Charting Tool</a>

<!-- pricing -->
<svg class="abs" style="left:0;top:1640px" width="1200" height="200" aria-hidden="true">
  <path d="M0 50C200 20 380 110 600 80C820 50 1000 20 1200 60V200H0Z" fill="var(--soft)" opacity=".6"/>
  <path d="M0 110C240 80 460 150 700 120C900 95 1060 90 1200 110V200H0Z" fill="#fff"/>
</svg>
<h2 class="abs center h2" style="top:1742px">Pricing Plan</h2>
<p class="abs center" style="top:1787px;font-size:13px;color:var(--muted);font-weight:300">You start with charting at $49/mon and then add features as you need them.</p>

<div class="abs band" role="img" aria-label="Group of hikers with backpacks looking out over misty mountains"></div>
<svg class="abs" style="left:0;top:2640px" width="1200" height="170" aria-hidden="true">
  <path d="M0 120C120 150 220 70 360 90C500 110 560 150 700 120C820 95 900 60 1040 90C1120 105 1170 60 1200 50V170H0Z" fill="#fff"/>
</svg>

<div class="card" style="left:129px">
  <div class="name">Free</div><hr>
  <div class="desc">Chart patient findings for FREE. Unlimited users, doctors, and location.</div>
  <div class="price">$0<sup>/ mo</sup></div>
  <div class="note">No strings attached</div>
  <a class="btn outline">Get Started Now!</a>
</div>
<div class="card" style="left:457px">
  <div class="pick">Pick</div>
  <div class="name">1 Add On <svg width="12" height="8"><path d="M1 1L6 6L11 1" stroke="var(--blue)" fill="none" stroke-width="1.4"/></svg></div><hr>
  <div class="desc">Choose between schedule, intake, bill, eligible, or review.</div>
  <div class="price">$99<sup>/ mo</sup></div>
  <div class="note">Per Location</div>
  <a class="btn">Get Started Now!</a>
</div>
<div class="card" style="left:785px">
  <div class="name">All Add Ons</div><hr>
  <div class="desc">Get all five features: schedule, intake, bill, eligible, and /or review.</div>
  <div class="price">$459<sup>/ mo</sup></div>
  <div class="note">Per Location</div>
  <a class="btn outline">Get Started Now!</a>
</div>

<div class="abs center club-small">Now spend time outside the office!</div>
<h2 class="abs center club-title">Become part of a club that wants to change the<br>way we practice, so we can have a<br>life outside of the office.</h2>
<a class="btn blue" style="left:521px;top:2483px;width:158px;height:38px">Join the Club</a>

<!-- signup form -->
<h2 class="abs center h2" style="top:2819px;line-height:36px">Get Started with a Free<br>Charting Tool</h2>
<div class="field" style="left:293px;top:2922px;width:297px">Full Name</div>
<div class="field" style="left:612px;top:2922px;width:295px">Your Email</div>
<div class="field" style="left:293px;top:2982px;width:190px">Cell Phone</div>
<div class="field" style="left:506px;top:2982px;width:189px">Office Name</div>
<div class="field" style="left:717px;top:2982px;width:190px">NPI</div>
<div class="field" style="left:293px;top:3042px;width:614px;height:94px">Message ...</div>
<a class="btn" style="left:497px;top:3177px;width:207px;height:38px">Get Free Charting Tool</a>
<div class="abs chat">
  <svg width="20" height="18" fill="none" stroke="#fff" stroke-width="1.6"><path d="M2 2H18V13H8L4 16V13H2Z"/><path d="M6 7.5H6.1M10 7.5H10.1M14 7.5H14.1" stroke-linecap="round" stroke-width="2"/></svg>
</div>

<!-- footer -->
<div class="abs footer-line"></div>
<div class="abs logo foot-logo">mirvo</div>
<div class="abs copy">2020 © Mirvo. All Rights Reserved.</div>
<span class="social" style="left:973px;background:var(--blue)"></span>
<span class="social" style="left:1001px;background:#6b7280"></span>
<span class="social" style="left:1031px;background:#6b7280"></span>
<span class="social" style="left:1059px;background:#6b7280"></span>

</body>
</html>
```